VALMORE INDUSTRIES est une société dont l'activité est orienté INDUSTRIE TECHNIQUE. Notre activité...

Ce flyer d‘une page doit décrire les principaux thèmes de nos activités
Il faut donc faire mentionner sur le flyer :
- LA FORMATION pompes, ATEX, robinetterie...
-Actualités industrielles ROUAGES D'USINE
-Le magazine VALMORE BREF HEBDO
- ATELIER OPTIMAL expertise, conseil...
Egalement écrire sur le flyer la phrase suivante :
VALMORE Industries vous présente son savoir faire
ainsi que notre adresse mail www.valmoreindustries-exemple.fr
et notre téléphone +33 (1) 55 20 61 39
Et bien sur ajouter notre logo qui est en pièce jointe
Ce flyer sera essentiellement distribué lors de grands salons d'expositions à nos clients et futurs clients. il sera également adressé par voie postale à nos lecteurs soit environ 15000 exemplaires
En vous remerciant par avance

```html
<!DOCTYPE html>
<html lang="fr">
<head>
<meta charset="utf-8">
<title>VALMORE INDUSTRIES – Flyer</title>
<link href="https://fonts.googleapis.com/css2?family=Montserrat:wght@400;500;600;700;800&family=Raleway:wght@400;500;600&display=swap" rel="stylesheet">
<style>
  :root{
    --green:#1f8a2e;
    --green-dark:#0f6a1e;
    --red:#e0261c;
    --ink:#2b2b2b;
    --grey:#555;
    --photo-dark:#2a2c2e;
    --photo-mid:#6d6f70;
    --white:#ffffff;
  }
  *{margin:0;padding:0;box-sizing:border-box}
  html,body{width:700px;height:1200px;overflow:hidden;background:#fff}
  .flyer{position:relative;width:700px;height:1200px;overflow:hidden;background:var(--white);font-family:"Montserrat",sans-serif;color:var(--ink)}
  .hero-photo{position:absolute;left:0;top:120px;width:700px;height:500px;
    background:radial-gradient(ellipse at 50% 40%,var(--photo-mid) 0%,#45484a 45%,var(--photo-dark) 100%)}
  .shapes{position:absolute;inset:0;width:700px;height:1200px}
  .brand{position:absolute;top:78px;left:0;width:700px;text-align:center}
  .brand-name{display:inline-flex;align-items:center;gap:10px;font-size:28px;font-weight:800;color:var(--green);letter-spacing:1px}
  .brand-name .dot{width:18px;height:18px;border-radius:50%;background:var(--green)}
  .headline{position:absolute;top:282px;left:0;width:700px;text-align:center;color:#fff}
  .headline .lead{display:inline-block;font-size:21px;font-weight:400;letter-spacing:.5px;padding-bottom:4px;border-bottom:1px solid #fff}
  .headline .expert{font-size:54px;font-weight:800;color:var(--red);line-height:1.05;letter-spacing:1px}
  .headline .topic{display:inline-block;font-size:21px;font-weight:400;padding-top:4px;border-top:1px solid #fff}
  .headline .fields{margin-top:14px;font-size:13.5px;font-weight:500;line-height:17px}
  .contact{position:absolute;top:664px;left:35px;width:300px;text-align:center}
  .contact h2{font-size:17px;font-weight:700;line-height:22px}
  .pin{display:block;margin:16px auto 4px}
  .address{font-size:11px;font-weight:500;line-height:15px}
  .call{margin-top:14px;font-size:14px;font-weight:600}
  .phone{margin:6px auto 0;width:265px;height:40px;border-radius:20px;background:linear-gradient(#2d9c3a,var(--green-dark));display:flex;align-items:center;color:#fff;font-size:22px;font-weight:600;overflow:hidden}
  .phone .ico{width:44px;height:40px;background:#8fc88f;display:flex;align-items:center;justify-content:center;margin-right:12px}
  .url{margin-top:10px;font-size:14.5px;font-weight:700}
  .social{margin-top:10px;display:flex;justify-content:center;gap:12px}
  .social span{width:25px;height:25px;border-radius:50%;border:2px solid var(--red)}
  .intro{position:absolute;top:666px;left:366px;width:300px;font-family:"Raleway",sans-serif;font-size:11.2px;line-height:15.5px;color:var(--grey);text-align:justify}
  .intro p+p{margin-top:12px}
  .topics{position:absolute;top:830px;left:366px;width:310px;display:grid;grid-template-columns:1fr 1fr;row-gap:14px;column-gap:8px;font-size:9.3px;font-weight:700;line-height:12px}
  .topics li{list-style:none;padding-left:13px;position:relative}
  .topics li::before{content:"»";position:absolute;left:0;top:-2px;color:var(--green);font-size:13px}
  .topics small{font-weight:600;font-size:9px}
  .photo-round{position:absolute;border-radius:50%;border:5px solid #fff;box-shadow:0 3px 8px rgba(0,0,0,.35)}
  .photo-pipes{left:40px;top:1003px;width:134px;height:134px;background:radial-gradient(circle at 50% 40%,#9a9c9e,#3b3d3f)}
  .photo-rotor{left:190px;top:1040px;width:124px;height:124px;background:radial-gradient(circle at 45% 45%,#f04a38,var(--red) 70%)}
  .partners{position:absolute;top:930px;left:356px;width:310px;height:220px;background:#fff;border-radius:12px;box-shadow:0 0 8px rgba(0,0,0,.2);display:grid;grid-template-columns:repeat(4,1fr);grid-template-rows:repeat(3,1fr);align-items:center;justify-items:center;padding:14px 10px}
  .badge{width:48px;height:22px;border-radius:4px;background:#cfd6dc}
  .badge.round{width:30px;height:30px;border-radius:50%;background:#d9463d}
  .badge.blue{background:#2f5fa8}
  .badge.green{background:#7ab648}
</style>
</head>
<body>
<main class="flyer">
  <div class="hero-photo" role="img" aria-label="Photo de canalisations industrielles en perspective, tons gris sombres"></div>

  <svg class="shapes" viewBox="0 0 700 1200" aria-hidden="true">
    <defs>
      <linearGradient id="headerGrad" x1="0" y1="0" x2="0" y2="1">
        <stop offset="0" stop-color="#e2e2e2"/><stop offset="1" stop-color="#ffffff"/>
      </linearGradient>
    </defs>
    <path d="M0,0 H700 V124 Q350,268 0,124 Z" fill="var(--green)"/>
    <path d="M0,0 H700 V112 Q350,246 0,112 Z" fill="#fff"/>
    <path d="M0,0 H700 V104 Q350,234 0,104 Z" fill="var(--red)"/>
    <path d="M0,0 H700 V98 Q350,222 0,98 Z" fill="url(#headerGrad)"/>
    <path d="M0,600 Q350,480 700,600 V1200 H0 Z" fill="var(--green)"/>
    <path d="M0,612 Q350,500 700,612 V1200 H0 Z" fill="#fff"/>
    <path d="M0,630 Q200,560 350,548 Q200,575 0,645 Z" fill="var(--red)"/>
    <path d="M700,630 Q500,560 350,548 Q500,575 700,645 Z" fill="var(--red)"/>
    <path d="M0,650 Q350,520 700,650 V1200 H0 Z" fill="#fff"/>
    <path d="M0,1010 Q330,1200 700,1100 V1200 H0 Z" fill="var(--green)"/>
    <path d="M0,1010 Q330,1200 700,1100" fill="none" stroke="#fff" stroke-width="3"/>
  </svg>

  <header class="brand">
    <p class="brand-name"><span class="dot"></span>VALMORE INDUSTRIES</p>
  </header>

  <section class="headline">
    <p class="lead">VOUS CHERCHEZ UN</p>
    <p class="expert">EXPERT</p>
    <p class="topic">DE LA FORMATION</p>
    <p class="fields">DE LE MAINTENANCE,<br>DES INDUSTRIES DE PROCESS,<br>DES POMPES,<br>DE L'ATEX...</p>
  </section>

  <section class="contact">
    <h2>VALMORE INDUSTRIES<br>VOUS PRÉSENTE SON<br>SAVOIR FAIRE</h2>
    <svg class="pin" width="16" height="22" viewBox="0 0 16 22"><path d="M8 0C3.6 0 0 3.5 0 7.8 0 13.5 8 22 8 22s8-8.5 8-14.2C16 3.5 12.4 0 8 0z" fill="var(--red)"/><circle cx="8" cy="8" r="3" fill="#fff"/></svg>
    <p class="address">42 Rue des Tanneurs<br>F-94270 Val-Coudray</p>
    <p class="call">Call</p>
    <p class="phone"><span class="ico"><svg width="18" height="18" viewBox="0 0 24 24"><path d="M6.6 10.8c1.4 2.8 3.8 5.1 6.6 6.6l2.2-2.2c.3-.3.7-.4 1-.2 1.1.4 2.3.6 3.6.6.6 0 1 .4 1 1V20c0 .6-.4 1-1 1C10.6 21 3 13.4 3 4c0-.6.4-1 1-1h3.5c.6 0 1 .4 1 1 0 1.3.2 2.5.6 3.6.1.3 0 .7-.2 1z" fill="#fff"/></svg></span>+33 (1) 5520 6139</p>
    <p class="url">www.valmoreindustries-exemple.fr</p>
    <div class="social"><span></span><span></span><span></span></div>
  </section>

  <section class="intro">
    <p>Chaque année, de nombreuses formations sont programmées sur la maintenance des pompes, sur le choix des pompes et le dimensionnement des installations de pompage.</p>
    <p>sur la sécurité ATEX, sur les bases de l'électricité en milieu industriel, sur la maintenance et le montage des roulements...</p>
  </section>

  <ul class="topics">
    <li>LA FORMATION pompes,<br>ATEX, robinetterie...</li>
    <li><small>Actualités industrielles</small><br>ROUAGES D'USINE</li>
    <li><small>Le magazine</small><br>VALMORE BREF HEBDO</li>
    <li>ATELIER OPTIMAL<br><small>expertise, conseil...</small></li>
  </ul>

  <div class="photo-round photo-pipes" role="img" aria-label="Photo circulaire de tuyauteries en acier"></div>
  <div class="photo-round photo-rotor" role="img" aria-label="Illustration d'un rotor de pompe à vis sur fond rouge"></div>

  <section class="partners" aria-label="Partenaires">
    <span class="badge round"></span><span class="badge blue"></span><span class="badge blue"></span><span class="badge green"></span>
    <span class="badge"></span><span class="badge round"></span><span class="badge"></span><span class="badge"></span>
    <span class="badge"></span><span class="badge blue"></span><span class="badge blue"></span><span class="badge blue"></span>
  </section>
</main>
</body>
</html>
```